Post Card Mailer Design-

Marbrook Elder Living is a subsidiary of the Marbrook Haven Group. This Post Card is specifically for the Marbrook Elder Living company and brand. Create a 4 x 6, front and back, Post Card. This Post Card will be an invitation to prospective clients and/or caring family members to join us for informative and personalized get together(s) to discuss the Senior Care Home that we are opening. It is a modern and state of the art home. Like the home, the Post Card must be eye catching, unique in its deliverables (as it doesn’t feel like a care facility) and demonstrate both attention to detail and comfort. Our organization is sophisticated and built around warmth, care and individualized personal attention. The most important aspect of this design is to focus on creating a nurturing, warm, and inviting feel that would attract a prospective client to want to join us for an educational event.

I am open to the creativity of the designer to develop something based on the above criteria; however I would like the design to work well with our existing collateral material. What I mean by that is that while I want everything to have its own personality and stand out as its own brand representative, I still need to be able to tell that the overall design concept stays stylistically inside of the same ‘family’ of existing designed material. Because of this, I would like for the designer to pull inspiration from the link to our website (Located below) as well as from our recently refreshed business cards (Attached Below). This should allow the Post Card design to be unique and creative, while still staying inside of a framework and the feel/style that I am looking for.

Finally, I want all the designers to understand that this Post Card design is for an educational and informative, small sized event where we are looking to attract attendance from prospective clients and/or caring family members of active, positive, and happy seniors/elders. We are responsible for providing personalized care for a culturally and ethnically diverse make-up of active, positive, and happy seniors/elders. The photos that are used must be tasteful, graceful, and elegant.
Updates

Industry/Entity Type

It Company

Requirements
Must have
• • The company logo must be included.•
• Look under the Marbrook Elder Living tab at www.marbrookhavengroup.net.

```html
<!DOCTYPE html>
<html lang="en">
<head>
<meta charset="utf-8">
<title>Marbrook Elder Living – Open House Post Card</title>
<link rel="stylesheet" href="https://fonts.googleapis.com/css2?family=Cormorant+Garamond:wght@500&family=Playfair+Display:ital@1&family=Montserrat:wght@500&display=swap">
<style>
  :root {
    --backdrop: #2f2f31;
    --teal: #4b9ba4;
    --teal-light: #7cbcc3;
    --teal-text: #5aa8b0;
    --paper: #f4f4f3;
    --white: #ffffff;
    --grey: #6d6e70;
  }
  * { margin: 0; padding: 0; box-sizing: border-box; }
  html, body { width: 1200px; height: 900px; overflow: hidden; }
  body { background: var(--backdrop); position: relative; }

  .card {
    position: absolute;
    top: 72px;
    width: 498px;
    height: 748px;
    overflow: hidden;
  }
  .card--front { left: 50px; background: var(--teal); }
  .card--back { left: 650px; background: var(--paper); }
  .card__art { position: absolute; inset: 0; width: 100%; height: 100%; }

  .brand {
    position: absolute;
    left: 0; right: 0;
    text-align: center;
  }
  .brand__mark {
    display: block;
    width: 74px; height: 68px;
    margin: 0 auto 30px;
    background: var(--teal);
    border-radius: 10px;
  }
  .brand__name {
    font-family: "Cormorant Garamond", serif;
    font-weight: 500;
    color: var(--grey);
    line-height: 1.05;
  }
  .brand__place {
    font-family: "Montserrat", sans-serif;
    font-weight: 500;
    color: var(--grey);
    letter-spacing: 0.42em;
    text-indent: 0.42em;
  }
  .tagline {
    font-family: "Playfair Display", serif;
    font-style: italic;
    color: var(--teal-text);
    text-align: center;
    line-height: 1.15;
  }
  .event-details {
    font-family: "Montserrat", sans-serif;
    font-weight: 500;
    color: var(--grey);
    font-size: 12px;
    line-height: 1.5;
    letter-spacing: 0.04em;
  }

  .card--front .brand { top: 218px; }
  .card--front .brand__name { font-size: 50px; }
  .card--front .brand__place { font-size: 15px; margin-top: 12px; }
  .card--front .tagline { font-size: 16px; margin-top: 10px; }

  .card--back .tagline--headline {
    position: absolute;
    top: 28px; left: 0; right: 0;
    font-size: 27px;
  }
  .card--back .brand { top: 580px; }
  .card--back .brand__name { font-size: 40px; }
  .card--back .brand__place { font-size: 13px; margin-top: 10px; }
  .card--back .event-details { margin-top: 12px; }
</style>
</head>
<body>

<section class="card card--front" aria-label="Post card front">
  <svg class="card__art" viewBox="0 0 498 748" aria-hidden="true">
    <ellipse cx="249" cy="373" rx="285" ry="228" fill="var(--teal-light)"/>
    <ellipse cx="249" cy="373" rx="250" ry="190" fill="var(--white)"/>
  </svg>
  <div class="brand">
    <span class="brand__mark" aria-hidden="true"></span>
    <p class="brand__name">Marbrook<br>Elder Living</p>
    <p class="brand__place">HALEWOOD</p>
    <p class="tagline">You're warmly invited...<br>Come meet our home.</p>
  </div>
</section>

<section class="card card--back" aria-label="Post card back">
  <p class="tagline tagline--headline">Join us for an informative open house<br>Saturday, May 17 · 2:00 PM</p>
  <svg class="card__art" viewBox="0 0 498 748">
    <defs>
      <clipPath id="photo-oval">
        <ellipse cx="265" cy="350" rx="300" ry="188"/>
      </clipPath>
      <linearGradient id="lounge-tone" x1="0" y1="0" x2="1" y2="1">
        <stop offset="0" stop-color="#b98d6e"/>
        <stop offset="1" stop-color="#6e5444"/>
      </linearGradient>
      <linearGradient id="bedroom-tone" x1="0" y1="0" x2="1" y2="1">
        <stop offset="0" stop-color="#d9c6a4"/>
        <stop offset="1" stop-color="#7a6450"/>
      </linearGradient>
      <linearGradient id="kitchen-tone" x1="0" y1="0" x2="1" y2="1">
        <stop offset="0" stop-color="#c9c2b4"/>
        <stop offset="1" stop-color="#7a2f22"/>
      </linearGradient>
    </defs>
    <ellipse cx="290" cy="345" rx="360" ry="224" fill="var(--teal)" aria-hidden="true"/>
    <g clip-path="url(#photo-oval)">
      <rect x="0" y="150" width="498" height="218" fill="url(#lounge-tone)" role="img" aria-label="Photo of a spacious lounge with a large leather sectional sofa"/>
      <rect x="0" y="370" width="263" height="180" fill="url(#bedroom-tone)" role="img" aria-label="Photo of a bright bedroom with curtained window"/>
      <rect x="265" y="370" width="233" height="180" fill="url(#kitchen-tone)" role="img" aria-label="Photo of a modern kitchen with wooden cabinets and granite island"/>
    </g>
  </svg>
  <div class="brand">
    <p class="brand__name">Marbrook<br>Elder Living</p>
    <p class="brand__place">HALEWOOD</p>
    <p class="event-details">418 Loma Lane, Halewood · RSVP (555) 014-2280<br>www.marbrookhavengroup.net</p>
  </div>
</section>

</body>
</html>
```